KORBALT

The business want a professional looking business card. We have a scetch we will add but want the extra upgrade, and would like more suggestions for variations of our business cards.

```html
<!DOCTYPE html>
<html lang="en">
<head>
<meta charset="UTF-8">
<title>KORBALT Business Card</title>
<link rel="stylesheet" href="https://fonts.googleapis.com/css2?family=Alegreya:wght@500;600&family=Mulish:wght@400;500&display=swap">
<style>
  :root {
    --backdrop: #e8e8e9;
    --card: #f3ece3;
    --ink: #4a2a17;
    --gold: #c4a272;
    --ornament-light: #ebdfcf;
    --ornament-mid: #e2d2bb;
  }
  * { margin: 0; padding: 0; box-sizing: border-box; }
  html, body { width: 1200px; height: 670px; overflow: hidden; }
  body {
    background: var(--backdrop);
    position: relative;
    font-family: "Mulish", sans-serif;
    color: var(--ink);
  }
  .card {
    position: absolute;
    top: 164px;
    width: 502px;
    height: 326px;
    background: var(--card);
    overflow: hidden;
  }
  .card--front { left: 68px; }
  .card--back { left: 635px; }

  .ornament-area {
    position: absolute;
    top: 0;
    right: 0;
    width: 175px;
    height: 100%;
    background:
      radial-gradient(ellipse 60% 35% at 55% 50%, var(--ornament-mid), transparent 75%),
      radial-gradient(ellipse 45% 30% at 95% 20%, var(--ornament-mid), transparent 75%),
      radial-gradient(ellipse 45% 30% at 95% 82%, var(--ornament-mid), transparent 75%),
      linear-gradient(90deg, transparent, var(--ornament-light));
  }

  .holder-name {
    position: absolute;
    left: 37px;
    top: 36px;
    font-family: "Alegreya", serif;
    font-weight: 500;
    font-size: 34px;
    line-height: 1;
    letter-spacing: 0.2px;
  }
  .holder-role {
    position: absolute;
    left: 37px;
    top: 82px;
    font-size: 20px;
    font-weight: 400;
  }
  .contact-row {
    position: absolute;
    left: 37px;
    top: 278px;
    display: flex;
    align-items: center;
    gap: 15px;
    font-size: 12.5px;
    white-space: nowrap;
  }
  .contact-item { display: flex; align-items: center; gap: 6px; }
  .contact-item svg { display: block; }

  .accent-rule {
    position: absolute;
    left: 77px;
    top: 42px;
    width: 2px;
    height: 242px;
    background: linear-gradient(180deg, #b8925f, var(--gold), #b8925f);
  }
  .brand-mark {
    position: absolute;
    left: 95px;
    width: 310px;
    top: 152px;
    text-align: center;
  }
  .brand-name {
    font-family: "Alegreya", serif;
    font-weight: 600;
    font-size: 40px;
    letter-spacing: 9px;
    line-height: 1;
    color: var(--ink);
  }
  .brand-since {
    margin-top: 12px;
    font-weight: 500;
    font-size: 13px;
    letter-spacing: 6px;
    color: var(--gold);
  }
  .brand-dot {
    position: absolute;
    left: 232px;
    top: 92px;
    width: 34px;
    height: 34px;
    border-radius: 50%;
    background: var(--gold);
  }
</style>
</head>
<body>
  <section class="card card--front">
    <div class="ornament-area" role="img" aria-label="Faint beige floral ornament pattern"></div>
    <h1 class="holder-name">Lars Henrik Solvang</h1>
    <p class="holder-role">CEO &amp; Founder</p>
    <div class="contact-row">
      <span class="contact-item">
        <svg width="10" height="16" viewBox="0 0 10 16"><rect x="1" y="1" width="8" height="14" rx="1.5" fill="none" stroke="#4a2a17" stroke-width="1.6"/><circle cx="5" cy="12.5" r="0.9" fill="#4a2a17"/></svg>
        004791846205
      </span>
      <span class="contact-item">
        <svg width="15" height="11" viewBox="0 0 15 11"><rect x="0.8" y="0.8" width="13.4" height="9.4" fill="none" stroke="#4a2a17" stroke-width="1.5"/><path d="M1 1 L7.5 6.5 L14 1" fill="none" stroke="#4a2a17" stroke-width="1.5"/></svg>
        korbalt.llc@postmail.com
      </span>
      <span class="contact-item">
        <svg width="14" height="14" viewBox="0 0 14 14" fill="none" stroke="#4a2a17" stroke-width="1.1"><circle cx="7" cy="7" r="6"/><ellipse cx="7" cy="7" rx="2.6" ry="6"/><path d="M1 7h12M2 4h10M2 10h10"/></svg>
        www.korbalt.llc
      </span>
    </div>
  </section>

  <section class="card card--back">
    <div class="ornament-area" role="img" aria-label="Faint beige floral ornament pattern"></div>
    <div class="accent-rule"></div>
    <div class="brand-dot"></div>
    <div class="brand-mark">
      <div class="brand-name">KORBALT</div>
      <div class="brand-since">SINCE 2026</div>
    </div>
  </section>
</body>
</html>
```